Spanish winery needs a label design for a red, white and rosé wine.

We need a front and back label for our representee Vidal Arandes SL, a wine producer in the Spanish region of Extremadura.

Trademark: Sereniza. Sereniza means balanced in English. The message is that the wine show the equilibrium of the blends specially produced for this project, it is balanced in the mounth and nose and it,s a good balance between quality and price.

Target: Wine targets entry level market retail sector in Europe so it cannot be too fancy.

Style: Spanish wines are better seen with a classic touch in the design although a bit of modernity is required.

Number of labels: 3 front and 3 back labels required although you can use the same design and just change the colors. Bottle is a bordeaux style 30 mm high with an screw cup closure, green for the red and transparent for the white and rosé.

Labels size: front max 90 (wide)x130 (high)mm. Back max 85 (w)x85(h)mm.

Information to include in the front label: Trademark, type of wine (red, white or rosé), two short lines of text with tasting notes (see texts on doc file), capacity 75cl, ABV:11º vol. Bottled by Vidal Arandes SL C/Tarifa 27. 06480 Villar del Conde (Badajoz). Spain.

Information to be included in the back label:trademark, type of wine, tasting notes (see texts on doc file), Capacity 75cl, Filling control mark: E, Barcode, Allergy advise, Contains sulfites advise, Pregnant women advise.

Paper: Shiny or matt paper with possibility of foil printing. No embossed effects.

Please see attached Vega Lunar label as a reference of the necessary information to be contained by labels.
Updates

Reason: We would like to give a bit more of time to those that have accepted and have not yet submitted a design.

Target Market(s)

Entry level european consumers

Industry/Entity Type

Retail

Requirements
Nice to have
• Maybe a clasical scale, old coins (balanced in cost).... Balance is the route to follow.

```html
<!DOCTYPE html>
<html lang="en">
<head>
<meta charset="utf-8">
<title>Sereniza Vino Rosado – Front and Back Labels</title>
<link rel="stylesheet" href="https://fonts.googleapis.com/css2?family=Crimson+Text:wght@400&display=swap">
<style>
  :root {
    --canvas: #ffffff;
    --label-paper: #ffffff;
    --label-edge: #a6a6a6;
    --ink: #2a2a2a;
    --rose-band: #d49b9c;
    --box-edge: #9a9a9a;
  }
  * { margin: 0; padding: 0; box-sizing: border-box; }
  html, body {
    width: 1200px; height: 1000px; overflow: hidden;
    background: var(--canvas);
  }
  body {
    position: relative;
    font-family: "Crimson Text", Georgia, serif;
    color: var(--ink);
  }
  .label {
    position: absolute;
    background: var(--label-paper);
    border: 1px solid var(--label-edge);
    overflow: hidden;
  }
  .brand-name {
    position: absolute; left: 0; right: 0;
    text-align: center;
    font-weight: 400;
    color: var(--ink);
    text-transform: uppercase;
  }

  /* Front label */
  .label--front { left: 138px; top: 192px; width: 451px; height: 574px; }
  .label--front .brand-name { top: 120px; font-size: 50px; letter-spacing: 8px; }
  .front-tagline {
    position: absolute; left: 0; right: 0; top: 258px;
    text-align: center; font-size: 24.5px; line-height: 32px;
  }
  .wine-type {
    position: absolute; left: 0; right: 0; top: 338px;
    text-align: center; font-size: 40px; letter-spacing: 3px;
  }
  .rose-band {
    position: absolute; left: 0; right: 0; bottom: 0; height: 149px;
    background: var(--rose-band);
  }
  .bottler {
    position: absolute; left: 0; right: 0; top: 34px;
    text-align: center; font-size: 13px; line-height: 18px;
  }
  .front-volume, .front-abv {
    position: absolute; bottom: 8px; font-size: 28px;
  }
  .front-volume { left: 10px; }
  .front-abv { right: 10px; }
  .estimated-mark { font-size: 36px; }

  /* Back label */
  .label--back { left: 617px; top: 222px; width: 425px; height: 425px; }
  .label--back .brand-name { top: 96px; font-size: 28px; letter-spacing: 5px; }
  .back-notes {
    position: absolute; left: 0; right: 0; top: 168px;
    text-align: center; font-size: 15px; line-height: 20px;
  }
  .info-box {
    position: absolute; top: 269px; width: 173px; height: 107px;
    border: 1px solid var(--box-edge);
    text-align: center; font-size: 15px; padding-top: 10px;
  }
  .info-box--allergy { left: 24px; }
  .info-box--barcode { left: 223px; }
  .back-volume, .back-abv {
    position: absolute; bottom: 10px; font-size: 17px;
  }
  .back-volume { left: 10px; }
  .back-abv { right: 10px; }
  .back-volume .estimated-mark { font-size: 20px; }
</style>
</head>
<body>

  <section class="label label--front" aria-label="Front label">
    <h1 class="brand-name">Sereniza</h1>
    <p class="front-tagline">A refreshing Spanish Rosado bursting<br>with ripe strawberry and cherry flavours.</p>
    <h2 class="wine-type">VINO ROSADO</h2>
    <div class="rose-band">
      <p class="bottler">Bottled by Vidal Arandes SL C/Tarifa 27.<br>06480 Villar del Conde (Badajoz).<br>Spain.</p>
      <span class="front-volume">75cl <span class="estimated-mark">e</span></span>
      <span class="front-abv">11% vol</span>
    </div>
  </section>

  <section class="label label--back" aria-label="Back label">
    <h2 class="brand-name">Sereniza</h2>
    <p class="back-notes">This fresh and elegant rosé wine features aromas of ripe<br>strawberry and flavours of juicy cranberry and cherry.<br>A great wine to drink on its own or with grilled chicken<br>and fish. Ready to drink now. Best served chilled.</p>
    <div class="info-box info-box--allergy">Allergy Advice</div>
    <div class="info-box info-box--barcode">Barcode</div>
    <span class="back-volume">75cl <span class="estimated-mark">e</span></span>
    <span class="back-abv">11% vol</span>
  </section>

</body>
</html>
```